Tidewater Ridge Podiatry

Please design a flyer using the same layout/font/colours ect as the business card (attached) please make the flyer with curved corners.
Front of DL flyer: (vertical)
Business name & logo (same as card attached)
Treatments include:
-foot, ankle & leg pain
-heel pain
-nail care
-corn & callus treatment
-bunion advice
-mechanical assessments
-orthotics
-nail surgery

Consulting within 'Bellwind Family Pharmacy' ApolloBay.
47-49 Tillbrook Parade, Marrowind Bay.
Call for appointments: 0411 837 260

Email:tidewaterridgepodiatry@pelmornmail.net

Reverse of flyer (horizontal)
Business name & logo

Derek Hollins
B.Pod.
B.App.Sci (HM)
NWMBQ Reg: Pod 0007384251

0422 716 308

RHS,KMB & LWF registered provider
Private Health Insurance-ancillaries cover.

```html
<!DOCTYPE html>
<html lang="en">
<head>
<meta charset="utf-8">
<title>Tidewater Ridge Podiatry – Flyer</title>
<link rel="stylesheet" href="https://fonts.googleapis.com/css2?family=Comfortaa:wght@500&family=Open+Sans:wght@400;700&display=swap">
<style>
:root{
  --bg:#ececec;
  --teal:#45bccd;
  --teal-pale:#d6f1f6;
  --white:#ffffff;
  --ink:#4a4a4a;
  --ink-soft:#5f5f5f;
  --slate:#58585a;
  --rule:#d9d9d9;
  --rule-dark:#6c6c6e;
  --photo-a:#f3c6b0;
  --photo-b:#f7a9b4;
  --photo-c:#f4d77a;
}
*{box-sizing:border-box;margin:0;padding:0}
html,body{width:1200px;height:910px;overflow:hidden;background:var(--bg)}
body{position:relative;font-family:"Open Sans",Arial,sans-serif}
.card{position:absolute;top:138px;width:535px;height:582px;border-radius:16px;overflow:hidden}
.card--front{left:50px;background:linear-gradient(160deg,var(--teal-pale) 0%,var(--white) 32%,var(--white) 100%);box-shadow:0 0 0 1px #dcdcdc}
.card--back{left:604px;background:var(--slate);color:var(--white);text-align:center}

.services{position:absolute;left:0;top:182px;list-style:none;z-index:1}
.services li{height:17px;margin-bottom:15px;width:430px;background:var(--teal);color:var(--white);font-weight:700;font-size:13.5px;line-height:17px;padding-left:24px;text-transform:uppercase;letter-spacing:.01em}
.front-art{position:absolute;inset:0;z-index:2}

.brand{position:absolute;text-align:center;font-family:"Comfortaa",sans-serif;font-weight:500;z-index:3}
.brand__mark{display:block;margin:0 auto 16px;border-radius:50%}
.brand__line{display:block;line-height:1.15}
.brand__line--sub{font-size:.66em;letter-spacing:.36em;padding-left:.36em}
.card--front .brand{left:20px;width:240px;top:62px;color:var(--teal);font-size:22px}
.card--front .brand__mark{width:34px;height:34px;background:var(--teal)}
.card--back .brand{left:0;width:100%;top:140px;color:var(--white);font-size:27px}
.card--back .brand__mark{width:44px;height:44px;border:3px solid var(--white)}

.front-footer{position:absolute;left:40px;right:40px;top:497px;border-top:1px solid var(--rule);padding-top:10px;text-align:center;color:var(--ink-soft);font-size:10px;line-height:15px;z-index:3}
.front-footer strong{display:block;color:var(--ink);font-size:11.5px;margin-bottom:2px}

.practitioner{position:absolute;left:0;width:100%;top:288px;font-size:13px;line-height:18px}
.practitioner strong{font-size:14px}
.contact{position:absolute;left:0;width:100%;top:360px;font-size:13px}
.contact svg{display:block;margin:0 auto 6px}
.back-footer{position:absolute;left:40px;right:40px;top:526px;border-top:1px solid var(--rule-dark);padding-top:10px;font-size:11.5px;line-height:18px}
</style>
</head>
<body>

<section class="card card--front" aria-label="Flyer front">
  <ul class="services">
    <li>Foot, ankle &amp; leg pain</li>
    <li>Heel pain</li>
    <li>Nail care</li>
    <li>Corn &amp; callus treatment</li>
    <li>Bunion advice</li>
    <li>Mechanical assessments</li>
    <li>Orthotics</li>
    <li>Nail surgery</li>
  </ul>

  <svg class="front-art" width="535" height="582" viewBox="0 0 535 582">
    <defs>
      <linearGradient id="photoTone" x1="0" y1="0" x2="1" y2="1">
        <stop offset="0" stop-color="var(--photo-b)"/>
        <stop offset=".45" stop-color="var(--photo-a)"/>
        <stop offset="1" stop-color="var(--photo-c)"/>
      </linearGradient>
    </defs>
    <circle cx="566" cy="180" r="292" fill="var(--teal)"/>
    <circle role="img" aria-label="Photo of hands massaging a foot beside a pink water lily" cx="564" cy="170" r="268" fill="url(#photoTone)"/>
  </svg>

  <div class="brand">
    <span class="brand__mark"></span>
    <span class="brand__line">Tidewater Ridge</span>
    <span class="brand__line brand__line--sub">Podiatry</span>
  </div>

  <footer class="front-footer">
    <strong>Consulting within 'Bellwind Family Pharmacy' MarrowindBay.</strong>
    47-49 Tillbrook Parade, Marrowind Bay.<br>
    Call for appointments: 0411 837 260<br>
    Email:tidewaterridgepodiatry@pelmornmail.net
  </footer>
</section>

<section class="card card--back" aria-label="Flyer reverse">
  <div class="brand">
    <span class="brand__mark"></span>
    <span class="brand__line">Tidewater Ridge</span>
    <span class="brand__line brand__line--sub">Podiatry</span>
  </div>

  <div class="practitioner">
    <strong>Derek Hollins</strong><br>
    B.Pod.B.App.Sci (HM)<br>
    NWMBQ Reg: Pod 0007384251
  </div>

  <div class="contact">
    <svg width="34" height="34" viewBox="0 0 34 34" aria-hidden="true">
      <circle cx="17" cy="17" r="15" fill="none" stroke="var(--white)" stroke-width="2"/>
      <path d="M12.5 9.5c1-.6 1.8-.2 2.3.7l1.2 2.3c.4.8.2 1.5-.5 2l-1 .7c.8 2 2.3 3.6 4.2 4.5l.8-1c.5-.6 1.3-.8 2-.4l2.3 1.3c.8.5 1.1 1.3.6 2.2-.8 1.4-2.2 2.2-3.8 1.8-4.6-1.2-8.2-4.9-9.3-9.6-.3-1.6.3-3.2 1.2-4.5z" fill="var(--white)"/>
    </svg>
    0422 716 308
  </div>

  <footer class="back-footer">
    RHS,KMB &amp; LWF registered provider<br>
    Private Health Insurance-ancillaries cover.
  </footer>
</section>

</body>
</html>
```